Business Card for my New Brokerage

Looking to get a business card design for my new Real Estate Brokerage.
I want it with Picture, Phone Number, Email, Website, Office Address
Name and Designation. Please add logo too.

Target Market(s)

Real Estate Investors or Home Buyers

Industry/Entity Type

Real Estate

Contact Information for Business Card

Name, Email, Phone Number, website, email, office address

Colors
EB3D1F
EC4F4E
F09395
F8D3D4
FCEDEE

Requirements
Must have
• Minimalistic, Clean, Modern, Photo
Nice to have
• White and Red Colors

```html
<!DOCTYPE html>
<html lang="en">
<head>
<meta charset="utf-8">
<title>Ember Realty Inc – Business Card</title>
<link href="https://fonts.googleapis.com/css2?family=Montserrat:wght@400;600;700&display=swap" rel="stylesheet">
<style>
  :root {
    --red: #d3232d;
    --red-deep: #b3141f;
    --gold: #c9a440;
    --gold-light: #e2c66f;
    --ink: #5b5f66;
    --card: #f7f8fa;
    --page: #e9ecf0;
    --suit: #1f232b;
  }
  * { margin: 0; padding: 0; box-sizing: border-box; }
  html, body { width: 1200px; height: 894px; overflow: hidden; }
  body {
    background: var(--page);
    font-family: "Montserrat", sans-serif;
    position: relative;
  }
  .card {
    position: absolute;
    left: 100px; top: 164px;
    width: 1000px; height: 566px;
    background: var(--card);
    border-radius: 34px;
    overflow: hidden;
    box-shadow: 0 14px 40px rgba(40, 50, 70, .18);
  }
  .brand {
    position: absolute;
    left: 45px; top: 62px;
    color: var(--red);
    font-weight: 600;
    text-align: center;
  }
  .brand-name {
    display: block;
    font-size: 92px;
    line-height: 1;
    letter-spacing: 1px;
  }
  .brand-sub {
    display: block;
    font-size: 30px;
    letter-spacing: 6px;
    margin-top: 8px;
  }
  .person {
    position: absolute;
    left: 45px; top: 234px;
  }
  .person-name {
    color: var(--red);
    font-weight: 700;
    font-size: 34px;
    letter-spacing: .5px;
  }
  .person-role {
    color: var(--ink);
    font-size: 26px;
    margin-top: 6px;
  }
  .contacts {
    position: absolute;
    left: 45px; top: 352px;
    list-style: none;
  }
  .contacts li {
    display: flex;
    align-items: center;
    gap: 12px;
    color: var(--ink);
    font-size: 26px;
    height: 36px;
  }
  .contacts svg { width: 24px; height: 24px; flex: none; }
  .portrait {
    position: absolute;
    left: 635px; top: 32px;
    width: 365px; height: 443px;
    background: linear-gradient(180deg, rgba(247,248,250,0) 0%, rgba(200,190,180,.5) 35%, var(--suit) 62%, var(--suit) 100%);
    border-radius: 160px 0 0 0;
  }
  .address-band {
    position: absolute;
    left: 0; top: 475px;
    width: 1000px; height: 58px;
    background: linear-gradient(90deg, var(--red-deep) 0%, var(--red) 45%, var(--red-deep) 80%, var(--gold) 88%, var(--gold-light) 100%);
    display: flex;
    align-items: center;
    padding-left: 105px;
    color: #fff;
    font-size: 25px;
  }
</style>
</head>
<body>
  <main class="card">
    <div class="brand">
      <span class="brand-name">EMBER</span>
      <span class="brand-sub">REALTY INC</span>
    </div>

    <section class="person">
      <h1 class="person-name">DANIEL HARROW</h1>
      <p class="person-role">Managing Director</p>
    </section>

    <ul class="contacts">
      <li>
        <svg viewBox="0 0 24 24"><circle cx="12" cy="12" r="12" fill="var(--red)"/><path d="M6 10c0-2 3-3 6-3s6 1 6 3l-2 1-1-2H9l-1 2z M8 12h8l1 5H7z" fill="#fff"/></svg>
        555 014 2290
      </li>
      <li>
        <svg viewBox="0 0 24 24"><circle cx="12" cy="12" r="12" fill="var(--red)"/><rect x="6" y="8" width="12" height="8" fill="none" stroke="#fff" stroke-width="1.6"/><path d="M6 8l6 5 6-5" fill="none" stroke="#fff" stroke-width="1.6"/></svg>
        info@emberrealty.com
      </li>
      <li>
        <svg viewBox="0 0 24 24"><circle cx="12" cy="12" r="12" fill="var(--red)"/><circle cx="12" cy="12" r="6.5" fill="none" stroke="#fff" stroke-width="1.5"/><path d="M5.5 12h13M12 5.5c-3 3.5-3 9.5 0 13M12 5.5c3 3.5 3 9.5 0 13" fill="none" stroke="#fff" stroke-width="1.2"/></svg>
        www.emberrealty.com
      </li>
    </ul>

    <div class="portrait" role="img" aria-label="Portrait photo of the managing director in a dark suit and red tie, arms crossed"></div>

    <footer class="address-band">Birch Lane, Ste 4, Millbrook, VT 05620</footer>
  </main>
</body>
</html>
```